Offer banner redesign / Simplifying existing banner

We have a banner there customer can click on to get an offer. We want to simplify this banner and to get it to at minimum. We are not clear about how it shoulderstand look like, but the actual banner you can see here (It's at the top of the page): https://ofenrohr-lagerhaus.de/kaminsysteme/ We want to get rid of the icons and to reduce the size of the baner. The baner shoulderstand contain the Following text: Affordable chimney using installation service button text: Request free quote

Target Market(s)

Customers from age of 40yrs.

Requirements
Must have
• Clear and good visible button
Nice to have
• It Should be simple and striking.

```html
<!DOCTYPE html>
<html lang="de">
<head>
<meta charset="utf-8">
<title>Angebotsbanner – Preiswerter Schornstein</title>
<link rel="stylesheet" href="https://fonts.googleapis.com/css2?family=Arimo:wght@400;700&display=swap">
<style>
  :root {
    --banner-bg-top: #f1f3f6;
    --banner-bg-bottom: #e9edf1;
    --headline-ink: #3b3b3d;
    --frame-border: #aeb6c9;
    --frame-fill: #f4f5f8;
    --cta-fill: #fab535;
    --cta-fill-dark: #f7ab2c;
    --cta-border: #e1981f;
    --cta-ink: #ffffff;
    --shadow-tone: #8d96a1;
  }
  html, body {
    margin: 0;
    padding: 0;
    width: 1200px;
    height: 171px;
    overflow: hidden;
  }
  .offer-banner {
    position: relative;
    width: 1200px;
    height: 171px;
    background: linear-gradient(180deg, var(--banner-bg-top), var(--banner-bg-bottom));
    font-family: "Arimo", "Helvetica Neue", Arial, sans-serif;
  }
  .offer-banner__headline {
    position: absolute;
    left: 45px;
    top: 28px;
    margin: 0;
    font-weight: 400;
    font-size: 43px;
    line-height: 51px;
    color: var(--headline-ink);
    white-space: nowrap;
  }
  .offer-banner__shadow {
    position: absolute;
    left: 600px;
    top: 133px;
    width: 600px;
    height: 22px;
  }
  .offer-banner__frame {
    position: absolute;
    left: 681px;
    top: 37px;
    width: 466px;
    height: 98px;
    border: 1px solid var(--frame-border);
    background: var(--frame-fill);
    box-sizing: border-box;
  }
  .offer-banner__cta {
    position: absolute;
    left: 8px;
    top: 8px;
    right: 8px;
    bottom: 8px;
    display: flex;
    align-items: center;
    justify-content: center;
    background: linear-gradient(180deg, var(--cta-fill), var(--cta-fill-dark));
    border: 1px solid var(--cta-border);
    color: var(--cta-ink);
    font-weight: 700;
    font-size: 26px;
    white-space: nowrap;
    text-decoration: none;
    text-shadow: 0 1px 1px rgba(150, 90, 0, 0.35);
  }
</style>
</head>
<body>
  <section class="offer-banner">
    <h2 class="offer-banner__headline">Preiswerter Schornstein<br>wahlweise mit Montageservice</h2>
    <svg class="offer-banner__shadow" viewBox="0 0 600 22" aria-hidden="true">
      <defs>
        <radialGradient id="frameShadow" cx="50%" cy="0%" r="50%">
          <stop offset="0%" stop-color="var(--shadow-tone)" stop-opacity="0.55"/>
          <stop offset="100%" stop-color="var(--shadow-tone)" stop-opacity="0"/>
        </radialGradient>
      </defs>
      <ellipse cx="300" cy="0" rx="300" ry="18" fill="url(#frameShadow)"/>
    </svg>
    <div class="offer-banner__frame">
      <a class="offer-banner__cta" href="#angebot">Kostenloses Angebot Anfordern</a>
    </div>
  </section>
</body>
</html>
```